2026 Company Line Card

We would like to redesign our current company line card. We send this printed flyer to prospective customers to introduce our company, the brands we represent, and our competitive advantages. Our website is www.valvorimsupply.com, and our phone number is (800) 312-4470. We're a specialty supplier for plumbing material, specifically water and life safety products. Our customers are mostly male, blue-collar contractors, ages 40-60. I have included a pdf of our current flyer and our high-resolution transparent logo. We would also like to highlight certain key points, which include:
Genuine OEM Parts
Technical Assistance from Repair Experts
Repair Information
1-2 day Delivery for the United States
Friendly & Knowledgeable Customer Service
The Largest Parts Inventory In The Nation
Testing Equipment
Full Service Gauge Calibration and Repair

```html
<!DOCTYPE html>
<html lang="en">
<head>
<meta charset="utf-8">
<title>Valvorim Supply Line Card</title>
<link href="https://fonts.googleapis.com/css2?family=Roboto+Condensed:wght@400;700&display=swap" rel="stylesheet">
<style>
:root{
  --navy:#1b3f8f;
  --blue-deep:#14306f;
  --red:#e0242f;
  --band-gray:#e6e6e6;
  --logo-bg:#ececec;
  --white:#ffffff;
  --page:#f4f4f4;
}
*{margin:0;padding:0;box-sizing:border-box}
html,body{width:1200px;height:641px;overflow:hidden;background:var(--page)}
.stage{position:relative;width:1200px;height:641px}
.flyer-frame{position:absolute;left:360px;top:10px;width:480px;height:620px;box-shadow:0 2px 6px rgba(0,0,0,.25)}
.flyer{position:absolute;left:0;top:0;width:820px;height:1060px;transform:scale(.5854);transform-origin:0 0;background:var(--white);overflow:hidden;font-family:"Roboto Condensed",Arial,sans-serif}
.flyer-shapes{position:absolute;left:0;top:0}
.brand{position:absolute;left:40px;top:34px;display:flex;align-items:center;gap:14px}
.brand-square{width:30px;height:30px;background:var(--red)}
.brand-name{font-size:40px;font-weight:400;color:var(--navy);letter-spacing:.5px}
.headline{position:absolute;left:515px;top:166px;color:var(--white);font-weight:700;font-size:27px;line-height:34px;letter-spacing:.5px}
.source-list{position:absolute;left:472px;top:258px;list-style:none;color:var(--white);font-weight:700;font-size:21px;letter-spacing:.5px}
.source-list li{display:flex;align-items:center;gap:12px;height:38px}
.why-title{position:absolute;left:440px;top:396px;display:flex;align-items:center;gap:16px;color:var(--blue-deep);font-weight:700;font-size:33px}
.features{position:absolute;left:202px;top:462px;display:grid;grid-template-columns:302px 300px;row-gap:12px;color:var(--navy);font-size:21px;line-height:23px}
.feature{display:flex;align-items:flex-start;gap:12px}
.feature svg{flex:none;margin-top:2px}
.brands{position:absolute;left:28px;top:668px;display:grid;grid-template-columns:repeat(5,84px);row-gap:22px}
.brands span{font-size:16px;font-weight:700;color:var(--blue-deep);text-align:center;line-height:24px;white-space:nowrap}
.web{position:absolute;left:30px;top:855px;color:var(--white);font-size:26px;font-weight:700;letter-spacing:1.5px}
.call{position:absolute;right:32px;top:852px;color:var(--white);font-weight:700;font-size:22px}
.call strong{font-size:36px;letter-spacing:.5px;margin-left:6px}
</style>
</head>
<body>
<div class="stage">
  <div class="flyer-frame">
    <div class="flyer">
      <svg class="flyer-shapes" width="820" height="1060" viewBox="0 0 820 1060">
        <defs>
          <linearGradient id="grille" x1="0" y1="0" x2="1" y2="1"><stop offset="0" stop-color="#d9d9d9"/><stop offset="1" stop-color="#6d6d6d"/></linearGradient>
          <linearGradient id="bluePanel" x1="0" y1="0" x2="1" y2="1"><stop offset="0" stop-color="#1c3f8c"/><stop offset="1" stop-color="#112a66"/></linearGradient>
          <linearGradient id="photoWorkbench" x1="0" y1="0" x2="1" y2="1"><stop offset="0" stop-color="#6b5a40"/><stop offset=".5" stop-color="#a58f55"/><stop offset="1" stop-color="#3f3a33"/></linearGradient>
          <linearGradient id="photoValve" x1="0" y1="0" x2="1" y2="1"><stop offset="0" stop-color="#b8b5ae"/><stop offset=".6" stop-color="#8a8680"/><stop offset="1" stop-color="#4b4845"/></linearGradient>
          <linearGradient id="photoParts" x1="0" y1="0" x2="1" y2="0"><stop offset="0" stop-color="#4d6b9a"/><stop offset=".4" stop-color="#a88a5a"/><stop offset="1" stop-color="#6b6660"/></linearGradient>
          <linearGradient id="footerDark" x1="0" y1="0" x2="1" y2="0"><stop offset="0" stop-color="#b0141c"/><stop offset="1" stop-color="#7a0d13"/></linearGradient>
        </defs>
        <polygon points="510,110 620,0 820,0 820,110" fill="url(#grille)"/>
        <g role="img" aria-label="Photo of a technician testing a backflow gauge at a workbench with tools and yellow hoses">
          <polygon points="0,110 510,110 205,415 0,415" fill="url(#photoWorkbench)"/>
        </g>
        <polygon points="510,110 820,110 820,390 440,390 415,415 205,415" fill="url(#bluePanel)"/>
        <polygon points="440,390 820,390 820,442 388,442" fill="var(--band-gray)"/>
        <polygon points="0,415 205,415 0,630" fill="var(--red)"/>
        <polygon points="55,448 64,474 92,474 70,490 78,516 55,500 32,516 40,490 18,474 46,474" fill="var(--white)"/>
        <rect x="0" y="630" width="820" height="215" fill="var(--logo-bg)"/>
        <g role="img" aria-label="Photo of a hand servicing the inside of a large stainless backflow valve">
          <polygon points="600,630 820,630 820,845 385,845" fill="url(#photoValve)"/>
        </g>
        <rect x="0" y="843" width="820" height="60" fill="var(--red)"/>
        <polygon points="0,843 420,843 360,903 0,903" fill="url(#footerDark)"/>
        <g role="img" aria-label="Photo strip of brass valve parts, springs and rubber seals on a workbench">
          <rect x="0" y="903" width="820" height="157" fill="url(#photoParts)"/>
        </g>
      </svg>

      <div class="brand"><span class="brand-square"></span><span class="brand-name">Valvorim Supply Company</span></div>

      <div class="headline">THE NATION'S LEADING<br>SOURCE FOR:</div>
      <ul class="source-list">
        <li><svg width="26" height="26" viewBox="0 0 24 24"><polygon points="12,1 15,9 23,9 16.5,14 19,22 12,17 5,22 7.5,14 1,9 9,9" fill="#fff"/></svg>GENUINE OEM PARTS</li>
        <li><svg width="26" height="26" viewBox="0 0 24 24"><polygon points="12,1 15,9 23,9 16.5,14 19,22 12,17 5,22 7.5,14 1,9 9,9" fill="#fff"/></svg>REPAIR INFORMATION</li>
        <li><svg width="26" height="26" viewBox="0 0 24 24"><polygon points="12,1 15,9 23,9 16.5,14 19,22 12,17 5,22 7.5,14 1,9 9,9" fill="#fff"/></svg>TECHNICAL ASSISTANCE</li>
      </ul>

      <div class="why-title">
        <svg width="24" height="24" viewBox="0 0 24 24"><polygon points="12,1 15,9 23,9 16.5,14 19,22 12,17 5,22 7.5,14 1,9 9,9" fill="var(--red)"/></svg>
        <span>WHY CHOOSE US?</span>
        <svg width="24" height="24" viewBox="0 0 24 24"><polygon points="12,1 15,9 23,9 16.5,14 19,22 12,17 5,22 7.5,14 1,9 9,9" fill="var(--red)"/></svg>
      </div>

      <div class="features">
        <div class="feature"><svg width="34" height="34" viewBox="0 0 24 24"><polygon points="12,2 22,6 22,18 12,22 2,18 2,6" fill="var(--navy)"/><polyline points="2,6 12,10 22,6 M12,10 12,22" fill="none" stroke="#fff" stroke-width="1.4"/></svg><span>1-2 Day Delivery Anywhere<br>in The US</span></div>
        <div class="feature"><svg width="34" height="34" viewBox="0 0 24 24"><rect x="8" y="2" width="8" height="8" fill="var(--navy)"/><rect x="2" y="12" width="9" height="9" fill="var(--navy)"/><rect x="13" y="12" width="9" height="9" fill="var(--navy)"/></svg><span>Largest Parts Inventory<br>In Nation</span></div>
        <div class="feature"><svg width="34" height="30" viewBox="0 0 24 24"><circle cx="12" cy="7" r="5" fill="var(--navy)"/><path d="M4 22c0-5 3.5-8 8-8s8 3 8 8z" fill="var(--navy)"/></svg><span>Repair Experts On Call</span></div>
        <div class="feature"><svg width="34" height="30" viewBox="0 0 24 24"><circle cx="12" cy="12" r="8" fill="none" stroke="var(--navy)" stroke-width="4" stroke-dasharray="3 2"/><circle cx="12" cy="12" r="3" fill="var(--navy)"/></svg><span>Testing Equipment</span></div>
        <div class="feature"><svg width="34" height="30" viewBox="0 0 24 24"><path d="M2 5l9 2v14l-9-2zM22 5l-9 2v14l9-2z" fill="var(--navy)"/></svg><span>Friendly Knowledgeable<br>Customer Service</span></div>
        <div class="feature"><svg width="34" height="30" viewBox="0 0 24 24"><path d="M4 4l16 16M20 4L4 20" stroke="var(--navy)" stroke-width="3.5" stroke-linecap="round"/></svg><span>Full Service Gauge<br>Department</span></div>
      </div>

      <div class="brands">
        <span>Alvenor</span><span>Ferrowick</span><span>Corvalen</span><span>Shelmarr</span><span>R.T.Q.</span>
        <span>Wexmoor</span><span>Milbrynn</span><span>Torvasta</span><span>Harbistow</span><span>Dunvasket</span>
        <span>Kelvrane</span><span>Thermbayle</span><span>Orvantis</span><span>Plainsgatter</span>
      </div>

      <div class="web">www.valvorimsupply.com</div>
      <div class="call">CALL US <strong>(800) 312-4470</strong></div>
    </div>
  </div>
</div>
</body>
</html>
```